Web Design For Staffing Company

We need a homepage web design for a technical staffing company.

Please see attached brief for project details.

please make the site modern with bold colors while matching the logo

Be sure to read the attached breif in full beforehand.

Target Market(s)

technical companies looking to hire talent

Industry/Entity Type

Staffing

Number of Pages Required

1 page

Font styles to use
Sans Serif

```html
<!DOCTYPE html>
<html lang="en">
<head>
<meta charset="utf-8">
<title>Corvane Staffing – Technical Staffing</title>
<link rel="stylesheet" href="https://fonts.googleapis.com/css2?family=Barlow:ital,wght@0,500;0,600;0,700;1,500&family=Poppins:ital,wght@0,400;0,500;0,600;1,500&display=swap">
<style>
:root{
  --navy:#163552;
  --navy-deep:#10283f;
  --blue:#3a8fd6;
  --blue-light:#5aa6e6;
  --ink:#222831;
  --text:#3b3f45;
  --muted:#7a7f87;
  --line:#e4e7eb;
  --white:#ffffff;
  --footer:#0c0d10;
}
*{box-sizing:border-box;margin:0;padding:0}
html,body{width:1200px;height:3125px;overflow:hidden;background:var(--white)}
body{position:relative;font-family:"Poppins",sans-serif;color:var(--text)}
.abs{position:absolute}
.btn{position:absolute;display:flex;align-items:center;justify-content:center;border-radius:20px;font-family:"Poppins",sans-serif;font-weight:600;font-size:12.5px;letter-spacing:.3px;text-transform:uppercase;color:var(--white);height:40px;width:143px}
.btn--navy{background:var(--navy)}
.btn--blue{background:var(--blue)}

/* hero */
.hero-photo{position:absolute;left:0;top:0;width:1200px;height:680px;border-radius:0 0 600px 600px/0 0 230px 230px;
  background:linear-gradient(180deg,#f4f4f4 0%,#ececec 45%,#d9d2cc 62%,#a98d7f 78%,#6d6a78 100%)}
.hero-title{position:absolute;top:168px;left:0;width:1200px;text-align:center;font-family:"Barlow",sans-serif;font-weight:700;font-size:38px;color:var(--navy);letter-spacing:.3px}
.hero-sub{position:absolute;top:216px;left:0;width:1200px;text-align:center;font-family:"Barlow",sans-serif;font-weight:500;font-size:27px;color:var(--ink);letter-spacing:.8px}

/* header */
.logo{position:absolute;left:234px;top:26px;display:flex;align-items:center;gap:10px}
.logo-dot{width:28px;height:28px;border-radius:50%;background:var(--blue)}
.logo-name{font-family:"Poppins",sans-serif;font-weight:600;font-size:20px;color:var(--navy)}
.search{position:absolute;left:483px;top:24px;width:482px;height:34px;border:1px solid var(--line);border-radius:17px;display:flex;overflow:hidden;background:var(--white);font-size:10.5px}
.search-field{width:197px;padding-left:16px;display:flex;align-items:center;color:#333}
.search-loc{width:146px;padding:0 14px;display:flex;align-items:center;justify-content:space-between;background:#f5f6f7;color:#333}
.search-btn{flex:1;background:var(--blue);color:var(--white);font-weight:600;font-size:10px;display:flex;align-items:center;justify-content:center;gap:8px}
.nav{position:absolute;left:234px;top:82px;width:731px;height:42px;background:var(--navy);display:flex;font-size:11.5px;font-weight:600;color:var(--white)}
.nav-item{display:flex;align-items:center;padding:0 21px;border-right:1px solid #24466a}
.nav-item--active{background:var(--blue);padding:0 23px}
.social{position:absolute;display:flex;gap:7px}
.social span{width:26px;height:26px;border-radius:50%;background:var(--white);display:block}
.social--dark span{background:var(--white)}

/* intro */
.intro{position:absolute;top:736px;left:300px;width:600px;text-align:center;font-size:14px;line-height:22.5px;color:#333;letter-spacing:.2px}
.intro b{color:var(--blue);font-weight:500}

/* split sections */
.photo{position:absolute}
.split-text{position:absolute;font-size:13.5px;line-height:22.5px;color:#333;letter-spacing:.2px;text-align:justify}
.split-text .accent{color:var(--blue)}

/* testimonial */
.testimonial{position:absolute;left:0;top:1564px;width:1200px;height:396px;background:radial-gradient(ellipse at 75% 30%,#e9eaec 0%,#f6f6f7 40%,#fbfbfb 70%,#f0f0f1 100%)}
.section-title{position:absolute;left:0;width:1200px;text-align:center;font-family:"Barlow",sans-serif;font-weight:600;font-size:30px;color:#121417}
.section-rule{position:absolute;left:584px;width:32px;height:2px;background:var(--blue)}
.quote{position:absolute;top:1724px;left:300px;width:600px;text-align:center;font-style:italic;font-weight:500;font-size:16.5px;line-height:22.5px;color:#1b1e22;letter-spacing:.6px}
.quote-name{position:absolute;top:1851px;left:0;width:1200px;text-align:center;font-size:19px;font-weight:500;color:var(--blue);letter-spacing:1px}
.quote-role{position:absolute;top:1881px;left:0;width:1200px;text-align:center;font-size:10.5px;color:#333}

/* blog */
.blog-band{position:absolute;left:0;top:1960px;width:1200px;height:130px;background:linear-gradient(180deg,#f3f3f4,#ffffff)}
.card{position:absolute;top:2105px;width:232px}
.card-photo{width:232px;height:149px}
.card-meta{margin-top:16px;display:flex;align-items:center;gap:6px;font-size:9.5px;color:var(--muted)}
.card-meta svg{flex:none}
.card-title{margin-top:9px;font-size:12.5px;font-weight:600;line-height:17.5px;color:var(--ink)}
.card-text{margin-top:7px;font-size:8.8px;line-height:16px;color:#444}
.card-more{margin-top:8px;font-size:8.5px;font-weight:600;color:var(--ink);display:flex;align-items:center;gap:5px}

/* cta */
.cta{position:absolute;top:2464px;width:356px;height:249px}
.cta--blue{background:linear-gradient(135deg,#2f86d4,#4a9de0 50%,#2a7cc6)}
.cta--navy{background:linear-gradient(135deg,#1a3e60,#163552 50%,#102a44)}
.cta-title{position:absolute;top:72px;left:0;width:100%;text-align:center;font-family:"Barlow",sans-serif;font-weight:600;font-size:20px;line-height:24px;color:var(--white)}
.cta-btn{position:absolute;top:137px;left:83px;width:190px;height:42px;border-radius:21px;background:var(--white);display:flex;align-items:center;justify-content:center;font-weight:600;font-size:12px;color:var(--navy)}

/* footer */
.footer{position:absolute;left:0;top:2782px;width:1200px;height:343px;background:var(--footer)}
.foot-col{position:absolute;top:2838px;width:230px}
.foot-head{font-weight:600;font-size:12px;color:var(--white)}
.foot-rule{margin-top:7px;width:26px;height:2px;background:var(--blue)}
.foot-text{margin-top:24px;font-size:10px;line-height:17.5px;color:#e6e6e6;height:54px}
.foot-btn{width:143px;height:38px;background:var(--blue);display:flex;align-items:center;justify-content:center;gap:10px;font-weight:600;font-size:10.5px;color:var(--white);margin-top:6px}
.foot-divider{position:absolute;left:0;top:3050px;width:1200px;height:1px;background:#1e2026}
.copyright{position:absolute;left:234px;top:3082px;font-size:9px;color:#9a9ea6}
.badge{position:absolute;left:732px;top:3071px;width:88px;height:35px;background:var(--white)}
</style>
</head>
<body>

<!-- hero -->
<div class="hero-photo" role="img" aria-label="Six smiling young professionals seated in a row against a white brick wall, using tablets, phones and laptops"></div>

<header>
  <div class="logo"><span class="logo-dot"></span><span class="logo-name">Corvane Staffing</span></div>
  <form class="search">
    <div class="search-field">Keyword</div>
    <div class="search-loc">Location
      <svg width="8" height="5" viewBox="0 0 8 5"><path d="M1 1l3 3 3-3" fill="none" stroke="#333" stroke-width="1.2"/></svg>
    </div>
    <div class="search-btn">
      <svg width="12" height="12" viewBox="0 0 12 12"><circle cx="5" cy="5" r="3.8" fill="none" stroke="#fff" stroke-width="1.5"/><path d="M8 8l3 3" stroke="#fff" stroke-width="1.5"/></svg>
      SEARCH JOBS
    </div>
  </form>
  <nav class="nav">
    <div class="nav-item nav-item--active">HOME</div>
    <div class="nav-item">ABOUT</div>
    <div class="nav-item">JOB SEEKERS</div>
    <div class="nav-item">CLIENTS</div>
    <div class="nav-item">CONTACT</div>
  </nav>
  <div class="social" style="left:832px;top:90px"><span></span><span></span><span></span><span></span></div>
</header>

<h1 class="hero-title">The Right People For The Right Jobs!</h1>
<p class="hero-sub">Bridging the talent gap in Technical Staffing</p>
<a class="btn btn--blue" style="left:447px;top:274px">Hire Talent</a>
<a class="btn btn--navy" style="left:610px;top:274px">Get Hired</a>

<p class="intro"><b>Corvane Staffing</b> is a National Technical Staffing and Recruiting Solutions Provider founded in 2013 focused on matching contract and full time Engineering and IT professionals with new and exciting employment opportunities!</p>

<!-- job seekers -->
<p class="split-text" style="left:234px;top:922px;width:333px"><span class="accent">Simply said… <b>WE LOVE TO RECRUIT!</b> It's our passion and we take it very seriously!</span> It is not easy for JOB SEEKERS to put their job search efforts and trust in the hands of someone else, especially when there are so many Staffing Firms to choose from. So how do you know you are choosing the best Staffing Representation possible?</p>
<a class="btn btn--navy" style="left:234px;top:1109px">Learn More</a>
<a class="btn btn--blue" style="left:391px;top:1109px">View Jobs</a>
<div class="photo" style="left:600px;top:865px;width:600px;height:350px;background:linear-gradient(120deg,#d8d6d0,#b8bcc0 35%,#5f7088 60%,#9aa0a6)" role="img" aria-label="Four colleagues seated in an office chatting with tablets and coffee cups"></div>

<!-- clients -->
<div class="photo" style="left:0;top:1215px;width:600px;height:349px;background:linear-gradient(110deg,#b9bcbe,#e3e2de 35%,#cfcac2 55%,#33415a 80%,#2a3040)" role="img" aria-label="A woman with a coffee mug talking with a colleague who takes notes on a notepad"></div>
<p class="split-text" style="left:635px;top:1271px;width:333px">Are you responsible for Technical Staffing within your organization? Are you satisfied with your current Supplier(s)' overall performance? Does it appear they identify potential Candidate(s) based purely on "buzz-word" searches? Is it evident they just do not grasp the scope and responsibilities of your technical staffing need(s)?</p>
<a class="btn btn--navy" style="left:635px;top:1458px">Learn More</a>
<a class="btn btn--blue" style="left:791px;top:1458px">Hire Talent</a>

<!-- testimonial -->
<section class="testimonial"></section>
<h2 class="section-title" style="top:1628px">TESTIMONIAL</h2>
<div class="section-rule" style="top:1676px"></div>
<svg class="abs" style="left:256px;top:1700px" width="76" height="56" viewBox="0 0 76 56">
  <path d="M4 40a12 12 0 1 0 12-12c0-10 6-18 16-22l-2-4C14 8 4 22 4 40z" fill="#9cc4ea"/>
  <path d="M40 40a12 12 0 1 0 12-12c0-10 6-18 16-22l-2-4C50 8 40 22 40 40z" fill="#9cc4ea"/>
</svg>
<blockquote class="quote">"Marcus Hale is an excellent recruiter. He is articulate, honest, has a good nature and is an effective information conduit between his clients and candidates. He gave me the feeling he is there for the big picture desiring to forge a future relationship that will be mutually beneficial to both of us."</blockquote>
<p class="quote-name">Sam R.</p>
<p class="quote-role">Electrical Test Engineer in the Automotive Sector</p>
<svg class="abs" style="left:966px;top:1758px" width="88" height="18" viewBox="0 0 88 18">
  <path d="M35 9H2M9 2L2 9l7 7" fill="none" stroke="#c5c8cc" stroke-width="1.5"/>
  <path d="M53 9h33M79 2l7 7-7 7" fill="none" stroke="var(--blue)" stroke-width="1.8"/>
</svg>

<!-- blog -->
<div class="blog-band"></div>
<h2 class="section-title" style="top:2006px">CORVANE BLOG</h2>
<div class="section-rule" style="top:2054px"></div>

<article class="card" style="left:234px">
  <div class="card-photo" style="background:linear-gradient(90deg,#9a9a9a,#3a3a3a 45%,#1c1c1c)" role="img" aria-label="Black and white portrait of an elderly scientist beside a quote about technology"></div>
  <div class="card-meta">
    <svg width="10" height="10" viewBox="0 0 10 10"><rect x="1" y="2" width="8" height="7" fill="none" stroke="#3a8fd6"/><path d="M1 4h8M3 1v2M7 1v2" stroke="#3a8fd6"/></svg>June 19, 2019
    <svg width="10" height="10" viewBox="0 0 10 10" style="margin-left:4px"><circle cx="5" cy="3.2" r="2.2" fill="none" stroke="#3a8fd6"/><path d="M1 9.5c0-2.5 2-4 4-4s4 1.5 4 4" fill="none" stroke="#3a8fd6"/></svg>corvanestaffing
  </div>
  <h3 class="card-title">Tips for Spotting a U.S. Recession Before It Becomes Official</h3>
  <p class="card-text">As the U.S. nears a record-long expansion in July, the conversation is increasingly turning to when it will all end.</p>
  <p class="card-more">READ MORE <svg width="9" height="5" viewBox="0 0 9 5"><path d="M0 2.5h8M6 .5l2 2-2 2" fill="none" stroke="#222" stroke-width=".9"/></svg></p>
</article>

<article class="card" style="left:484px">
  <div class="card-photo" style="background:linear-gradient(90deg,#e4eee8,#c9d4d6 40%,#2e4a78 70%,#34373d)" role="img" aria-label="A woman typing on a laptop at a desk"></div>
  <div class="card-meta">
    <svg width="10" height="10" viewBox="0 0 10 10"><rect x="1" y="2" width="8" height="7" fill="none" stroke="#3a8fd6"/><path d="M1 4h8M3 1v2M7 1v2" stroke="#3a8fd6"/></svg>June 17, 2019
    <svg width="10" height="10" viewBox="0 0 10 10" style="margin-left:4px"><circle cx="5" cy="3.2" r="2.2" fill="none" stroke="#3a8fd6"/><path d="M1 9.5c0-2.5 2-4 4-4s4 1.5 4 4" fill="none" stroke="#3a8fd6"/></svg>corvanestaffing
  </div>
  <h3 class="card-title">Ways To Make The Most Of The Hot Job Market</h3>
  <p class="card-text">"This is the tightest labor market I can remember. Unemployment is at a 50-year low and wage growth is at 3.2%," said Dana Price, chief economist…</p>
  <p class="card-more">READ MORE <svg width="9" height="5" viewBox="0 0 9 5"><path d="M0 2.5h8M6 .5l2 2-2 2" fill="none" stroke="#222" stroke-width=".9"/></svg></p>
</article>

<article class="card" style="left:734px">
  <div class="card-photo" style="background:linear-gradient(180deg,#c8d6e4,#e6ebef 40%,#8a8f94 70%,#5b5e62)" role="img" aria-label="Elevated highway bridge under construction with concrete piers"></div>
  <div class="card-meta">
    <svg width="10" height="10" viewBox="0 0 10 10"><rect x="1" y="2" width="8" height="7" fill="none" stroke="#3a8fd6"/><path d="M1 4h8M3 1v2M7 1v2" stroke="#3a8fd6"/></svg>June 6, 2019
    <svg width="10" height="10" viewBox="0 0 10 10" style="margin-left:4px"><circle cx="5" cy="3.2" r="2.2" fill="none" stroke="#3a8fd6"/><path d="M1 9.5c0-2.5 2-4 4-4s4 1.5 4 4" fill="none" stroke="#3a8fd6"/></svg>corvanestaffing
  </div>
  <h3 class="card-title">Back To Basics: Meeting Employees' Needs To Improve Organizational Performance</h3>
  <p class="card-text">The benefits of employee satisfaction are <span style="color:var(--blue);text-decoration:underline">well-established</span>, so HR professionals and leaders…</p>
  <p class="card-more">READ MORE <svg width="9" height="5" viewBox="0 0 9 5"><path d="M0 2.5h8M6 .5l2 2-2 2" fill="none" stroke="#222" stroke-width=".9"/></svg></p>
</article>

<!-- calls to action -->
<div class="cta cta--blue" style="left:234px">
  <h3 class="cta-title">LOOING FOR CAREER-MINDED<br>CANDIDATES?</h3>
  <a class="cta-btn">REQUEST TALENT</a>
</div>
<div class="cta cta--navy" style="left:609px">
  <h3 class="cta-title">LOOING FOR CAREER<br>OPPORTUNITIES?</h3>
  <a class="cta-btn">SEARCH JOBS</a>
</div>

<!-- footer -->
<footer class="footer"></footer>
<div class="foot-col" style="left:234px">
  <h4 class="foot-head">GET HIRED</h4><div class="foot-rule"></div>
  <p class="foot-text">Search our extensive list of available jobs to find your ideal match.</p>
  <a class="foot-btn"><svg width="12" height="12" viewBox="0 0 12 12"><circle cx="5" cy="5" r="3.8" fill="none" stroke="#fff" stroke-width="1.5"/><path d="M8 8l3 3" stroke="#fff" stroke-width="1.5"/></svg>SEARCH NOW</a>
</div>
<div class="foot-col" style="left:485px">
  <h4 class="foot-head">HIRE TALENT</h4><div class="foot-rule"></div>
  <p class="foot-text">We're here to provide the people you need to get work done.</p>
  <a class="foot-btn"><svg width="12" height="12" viewBox="0 0 12 12"><circle cx="6" cy="3.5" r="3" fill="#fff"/><path d="M0.5 12c0-3.5 2.5-5 5.5-5s5.5 1.5 5.5 5z" fill="#fff"/></svg>START TODAY</a>
</div>
<div class="foot-col" style="left:735px">
  <h4 class="foot-head">GET IN TOUCH</h4><div class="foot-rule"></div>
  <p class="foot-text">Corvane Staffing, Inc.<br>48 Harbor Lane, Suite 210<br>Milford, MA 01757</p>
  <a class="foot-btn"><svg width="13" height="10" viewBox="0 0 13 10"><rect width="13" height="10" rx="1" fill="#fff"/><path d="M0.5 1l6 4.5 6-4.5" fill="none" stroke="#3a8fd6" stroke-width="1.2"/></svg>CONTACT US</a>
</div>
<div class="foot-divider"></div>
<p class="copyright">Copyright © 2020 Corvane Staffing. All Rights Reserved</p>
<div class="badge" role="img" aria-label="Employment verification program badge"></div>
<div class="social social--dark" style="left:844px;top:3076px"><span></span><span></span><span></span><span></span></div>

</body>
</html>
```